Flyer Design Project

I need to create a flyer to advertise an Luxury Self Catering Apartment Complex in a Ski Resort in Europe. The development offers luxury accommodation to those who are on a budget.

Below is what needs to be included and a basic layout design idea i had that can be changed. The information is important. Hoping to get it on a flyer sized 21.6 x 14 cm

Title - 'Luxury Self Catering Ski Apartments For Rent'
Sub Title - 'Located 200m from Gondola, Restaurants and Bars'

Studio - Sleeps 1-2 - From only £200 per week
1 Bed - Sleeps 2-4 - From only £250 per week
2 Bed - Sleeps 4-6 - From only £350 per week

Image 1 Image 2 Image 3

- Fully Furnished Modern, Spacious & Comfortable Apartments
- Fully Staffed Development (Reception, Bar + Daily Cleaning)
- Family friendly & suitable for children of all ages

(Twitter Icon) @snowlarkchalets
E-mail - snowlarkchalets@mailvora.co.uk
Telephone - +44 (0) 7811 302 684

Target Market(s)

Our target market is very wide. We are trying to attract students, couples and families who are skiing on a budget.

Industry/Entity Type

Accommodation

Requirements
Must have
• The text contained in 'task description' is important but i'd like to be led on design. Size of around 21.6 x 14cm is important and i'd like the 3 images below (hopefully someone can get of the date and time in orange bottom right of all pics)

http://i2217.picvaultra.com/albums/kq412/tmwimages/Bansko/699_00_640_zpsd7b2ba81.jpeg

http://i2217.picvaultra.com/albums/kq412/tmwimages/Bansko/a_02_zps7503dd10.jpeg

http://i2217.picvaultra.com/albums/kq412/tmwimages/Bansko/699_08_640_zps2f11bf21.jpeg

```html
<!DOCTYPE html>
<html lang="en">
<head>
<meta charset="utf-8">
<title>Luxury Self Catering Ski Apartments – Flyer</title>
<link rel="stylesheet" href="https://fonts.googleapis.com/css2?family=Alfa+Slab+One&family=Didact+Gothic&family=PT+Sans:wght@400;700&display=swap">
<style>
  :root{
    --maroon:#5a1418;
    --maroon-dark:#3d0b0e;
    --maroon-mid:#7a2024;
    --gold:#e9a83a;
    --gold-deep:#c8841f;
    --title-gold:#f5c23c;
    --cream:#fbf1d6;
    --cream-deep:#f1dca8;
    --ink:#4a1014;
    --stage:#2a2a2a;
  }
  html,body{margin:0;padding:0;overflow:hidden;}
  body{width:1200px;height:900px;background:var(--stage);position:relative;}
  .flyer{
    position:absolute;left:310px;top:20px;width:580px;height:860px;
    background:var(--cream);overflow:hidden;
    box-shadow:0 6px 24px rgba(0,0,0,.45);
  }
  .hero-photo{
    position:absolute;left:0;top:110px;width:580px;height:330px;
    background:linear-gradient(180deg,#e8ecef 0%,#cfc6b8 35%,#9b8770 65%,#5c4a3a 100%);
  }
  .shapes{position:absolute;left:0;top:0;}
  .title{
    position:absolute;left:0;top:14px;width:580px;text-align:center;margin:0;
    font-family:"Alfa Slab One",serif;font-weight:400;font-size:22px;
    color:var(--title-gold);letter-spacing:.2px;
  }
  .subtitle{
    position:absolute;left:0;top:46px;width:580px;text-align:center;margin:0;
    font-family:"Didact Gothic",sans-serif;font-size:20px;color:#fff;
  }
  .room-photo{
    position:absolute;left:28px;width:164px;height:92px;
    border:5px solid var(--gold);border-radius:2px;
    box-shadow:0 2px 6px rgba(0,0,0,.35);
  }
  .room-photo.bedroom{top:428px;background:linear-gradient(135deg,#6b4228,#c59866 55%,#f3e6d2);}
  .room-photo.lounge{top:538px;background:linear-gradient(135deg,#d8d1c6,#8a7560 55%,#3a2a20);}
  .room-photo.kitchen{top:648px;background:linear-gradient(135deg,#2a1d16,#6c4a32 55%,#c9b9a5);}
  .list{
    position:absolute;left:212px;margin:0;padding:0;list-style:none;
    font-family:"PT Sans",sans-serif;font-size:15.5px;line-height:1.2;color:var(--ink);
  }
  .list li{position:relative;padding-left:14px;margin-bottom:8px;}
  .list li::before{
    content:"";position:absolute;left:0;top:6px;width:7px;height:7px;
    border-radius:50%;background:var(--ink);
  }
  .features{top:432px;width:350px;}
  .prices{top:590px;width:360px;}
  .prices li{margin-bottom:14px;}
  .price{font-weight:700;font-size:19px;}
  .contact{
    position:absolute;left:0;top:770px;width:580px;height:90px;
    font-family:"PT Sans",sans-serif;color:#fff;font-size:15.5px;
  }
  .contact-heading{position:absolute;left:44px;top:12px;margin:0;font-size:15px;font-weight:400;letter-spacing:.3px;}
  .contact-line{position:absolute;display:flex;align-items:center;gap:8px;margin:0;}
  .contact-line.phone{left:26px;top:32px;}
  .contact-line.email{left:26px;top:56px;}
  .contact-line.social{left:310px;top:56px;}
  .contact-line svg{flex:none;}
  .social-square{width:13px;height:13px;background:var(--gold);border-radius:2px;flex:none;}
</style>
</head>
<body>
  <article class="flyer">
    <div class="hero-photo" role="img" aria-label="Photograph of the stone and white-rendered apartment building with balconies and mountains behind"></div>

    <svg class="shapes" width="580" height="860" viewBox="0 0 580 860" aria-hidden="true">
      <defs>
        <linearGradient id="headerFill" x1="0" y1="0" x2="0" y2="1">
          <stop offset="0" stop-color="var(--maroon-mid)"/>
          <stop offset="1" stop-color="var(--maroon-dark)"/>
        </linearGradient>
        <linearGradient id="creamFill" x1="0" y1="0" x2="0" y2="1">
          <stop offset="0" stop-color="var(--cream-deep)"/>
          <stop offset="1" stop-color="var(--cream)"/>
        </linearGradient>
      </defs>
      <!-- header band -->
      <path d="M0 0 H580 V112 C470 132 330 100 180 126 C110 138 50 146 0 142 Z" fill="url(#headerFill)"/>
      <path d="M120 150 C260 118 420 136 580 108" fill="none" stroke="var(--gold)" stroke-width="7"/>
      <!-- cream info panel -->
      <path d="M0 420 C140 380 320 440 580 398 V780 H0 Z" fill="url(#creamFill)"/>
      <path d="M0 420 C140 380 320 440 580 398" fill="none" stroke="var(--gold-deep)" stroke-width="8"/>
      <!-- footer band -->
      <path d="M0 772 C180 748 380 792 580 760 V860 H0 Z" fill="url(#headerFill)"/>
      <path d="M0 772 C180 748 380 792 580 760" fill="none" stroke="var(--gold)" stroke-width="4"/>
    </svg>

    <h1 class="title">Luxury Self Catering Ski Apartments For Rent</h1>
    <p class="subtitle">Located 200m from Gondola, Restaurants and Bars</p>

    <div class="room-photo bedroom" role="img" aria-label="Photograph of an apartment bedroom with double bed"></div>
    <div class="room-photo lounge" role="img" aria-label="Photograph of an apartment living room with sofa and curtains"></div>
    <div class="room-photo kitchen" role="img" aria-label="Photograph of an apartment kitchen and dining area"></div>

    <ul class="list features">
      <li>Fully Furnished Modern,<br>Spacious &amp; Comfortable Apartments</li>
      <li>Fully Staffed Development<br>(Reception, Bar + Daily Cleaning)</li>
      <li>Family friendly &amp; suitable for children of all ages</li>
    </ul>

    <ul class="list prices">
      <li>Studio - Sleeps 1-2 - From only <span class="price">£200</span> per week</li>
      <li>1 Bed - Sleeps 2-4 - From only <span class="price">£250</span> per week</li>
      <li>2 Bed - Sleeps 4-6 - From only <span class="price">£350</span> per week</li>
    </ul>

    <footer class="contact">
      <h2 class="contact-heading">CONTACT US</h2>
      <p class="contact-line phone">
        <svg width="12" height="14" viewBox="0 0 12 14" aria-hidden="true"><path d="M3 1 L5 4 L4 5.5 C4.6 7.5 5.6 8.8 7 9.8 L8.5 8.8 L11 11 L9.5 13 C5 12.5 1 7.5 1 2.5 Z" fill="var(--gold)"/></svg>
        <span>+44 (0) 7811 302 684</span>
      </p>
      <p class="contact-line email">
        <svg width="13" height="10" viewBox="0 0 13 10" aria-hidden="true"><rect x="0.5" y="0.5" width="12" height="9" fill="var(--gold)"/><path d="M0.5 0.5 L6.5 5.5 L12.5 0.5" fill="none" stroke="var(--maroon)" stroke-width="1"/></svg>
        <span>snowlarkchalets@mailvora.co.uk</span>
      </p>
      <p class="contact-line social">
        <span class="social-square"></span>
        <span>@snowlarkchalets</span>
      </p>
    </footer>
  </article>
</body>
</html>
```